Referral Card thats different from the rest

Business card size-

Referral card that will be given to clients, in turn they will pass it on to their friends.

The referee will add their name and address, and friends name to card before it is passed on

Referee gets 2 FREE movie tickets

Friend gets $25 OFF their service

Company is an electrical contracting company specialising in the domestic market.

I would like the card to be fun not so serious!
Completely open minded to any and every creative idea!

attached is 2 photo of an example of what another business has, i am trying to achieve something similiar
Updates

I have increased the budget, ;)

i have added 2 x photos of what i am trying to achieve. this is from another business, I am after something similar to this
Thanks

I have updated the design brief.
this should help make it easir and more clear
Thanks

Target Market(s)

Home owners from 30yrs +

Industry/Entity Type

Electrical

Requirements
Must have
• Logo - Not a main feature of card
1300 574 862 on both sides
Lic no: 381946D (doesn’t have to be big) prefer on back

The main feature of the front of the card is the 2 free movie tickets for Referee & $25 OFF Friends first bill

HOW ABOUT TWO FREE MOVIE TICKETS?
It is easy! Know someone who needs an electrician? Maybe a friend, family member, relative or work colleague.
Tell them about us, and we will take $25 off their first bill and give you two FREE Movie Tickets just for introducing us.
To make a referral fill out this card and give it to your friend.

Recommended By:____________
Address:__________________
Frinds name: _____________

*this offer is only valued for work over $55. Non transferable for cash. This coupon is limited to 1 per customer, not to be used in conjunction with any other offer
Nice to have
• Catchy heading on card
example- tell a friend for cash card, (if i was giving away cash vouchers..)

example- keep me in your wallet and pass me on

```html
<!DOCTYPE html>
<html lang="en">
<head>
<meta charset="utf-8">
<title>Bright Spark Electrical – Referral Card</title>
<link rel="stylesheet" href="https://fonts.googleapis.com/css2?family=Sniglet&family=Chewy&display=swap">
<style>
  :root {
    --blue: #3a44c9;
    --blue-soft: #8c93e0;
    --white: #ffffff;
    --brown: #6a2a1c;
    --orange: #c4541f;
    --ink: #111111;
    --rule: #6a2a1c;
  }
  html, body {
    margin: 0;
    padding: 0;
    width: 1200px;
    height: 2253px;
    overflow: hidden;
    background: var(--white);
  }
  .canvas {
    position: relative;
    width: 1200px;
    height: 2253px;
    overflow: hidden;
    background: var(--white);
    font-family: "Sniglet", sans-serif;
  }

  /* ---------- Front face ---------- */
  .front-face {
    position: absolute;
    left: 0; top: 0;
    width: 1200px; height: 750px;
    background: radial-gradient(ellipse 560px 520px at 860px 150px, var(--blue) 0%, var(--blue-soft) 40%, rgba(255,255,255,0) 100%);
  }
  .brand {
    position: absolute;
    display: flex;
    align-items: center;
    gap: 14px;
    color: var(--brown);
    font-family: "Sniglet", sans-serif;
    font-weight: 400;
    line-height: 1.05;
  }
  .brand-dot {
    flex: none;
    border-radius: 50%;
    background: var(--orange);
  }
  .front-face .brand {
    left: 24px; top: 70px;
    width: 290px;
    font-size: 34px;
  }
  .front-face .brand-dot { width: 34px; height: 34px; }

  .headline {
    position: absolute;
    left: 330px; top: 50px;
    margin: 0;
    font-family: "Chewy", cursive;
    font-weight: 400;
    font-size: 46px;
    letter-spacing: 1px;
    color: var(--brown);
    text-transform: uppercase;
  }
  .pitch {
    position: absolute;
    left: 250px; top: 168px;
    width: 900px;
    margin: 0;
    text-align: center;
    font-size: 28px;
    line-height: 41px;
    color: var(--orange);
  }
  .form-field {
    position: absolute;
    left: 45px;
    display: flex;
    align-items: flex-end;
    font-size: 33px;
    color: var(--brown);
  }
  .form-field .fill-line {
    display: inline-block;
    margin-left: 12px;
    margin-bottom: 8px;
    border-bottom: 3px dotted var(--rule);
  }
  .field-recommended { top: 372px; }
  .field-recommended .fill-line { width: 680px; }
  .field-address { top: 452px; }
  .field-address .fill-line { width: 880px; }
  .field-friend { top: 538px; }
  .field-friend .fill-line { width: 808px; }

  .fine-print {
    position: absolute;
    left: 160px; top: 608px;
    width: 960px;
    margin: 0;
    font-size: 19px;
    line-height: 34px;
    color: var(--orange);
  }
  .phone {
    position: absolute;
    margin: 0;
    font-size: 36px;
    color: var(--brown);
  }
  .front-face .phone { left: 515px; top: 694px; }

  /* ---------- Side labels ---------- */
  .face-label {
    position: absolute;
    display: flex;
    align-items: center;
    gap: 24px;
    font-size: 40px;
    color: var(--ink);
  }
  .face-label svg { flex: none; }
  .label-front { left: 380px; top: 812px; }
  .label-back { left: 380px; top: 1232px; }

  /* ---------- Back face ---------- */
  .back-face {
    position: absolute;
    left: 0; top: 1500px;
    width: 1200px; height: 753px;
    background: radial-gradient(ellipse 460px 640px at 1200px 130px, var(--blue) 0%, var(--blue-soft) 38%, rgba(255,255,255,0) 100%);
  }
  .back-face .brand {
    left: 180px; top: 200px;
    width: 320px;
    font-size: 42px;
  }
  .back-face .brand-dot { width: 40px; height: 40px; }
  .tagline {
    position: absolute;
    left: 0; top: 600px;
    width: 1200px;
    margin: 0;
    text-align: center;
    font-size: 32px;
    color: var(--orange);
  }
  .back-face .phone { left: 457px; top: 688px; }
  .licence {
    position: absolute;
    left: 930px; top: 700px;
    margin: 0;
    font-size: 24px;
    color: var(--orange);
  }
</style>
</head>
<body>
<div class="canvas">

  <section class="front-face">
    <div class="brand"><span class="brand-dot"></span><span>Bright Spark Electrical Pty Ltd</span></div>
    <h1 class="headline">How about two free movie tickets?</h1>
    <p class="pitch">
      It is easy! Know someone who needs an electrician?<br>
      Maybe a friend, family member, relative or work colleague,<br>
      Tell them about us, and we will take $25 off their first bill<br>
      and give you two FREE Movie Tickets just for introducing us
    </p>
    <div class="form-field field-recommended">Recommended By:<span class="fill-line"></span></div>
    <div class="form-field field-address">Address:<span class="fill-line"></span></div>
    <div class="form-field field-friend">Frinds name:<span class="fill-line"></span></div>
    <p class="fine-print">
      *this offer is only valued for work over $55. Non transferable for cash. This coupon<br>
      is limited to 1 per customer, not to be used in conjunction with any other offer
    </p>
    <p class="phone">1300 574 862</p>
  </section>

  <div class="face-label label-front">
    <svg width="80" height="195" viewBox="0 0 80 195" aria-hidden="true">
      <line x1="40" y1="195" x2="40" y2="14" stroke="#111" stroke-width="9"/>
      <polyline points="4,50 40,10 76,50" fill="none" stroke="#111" stroke-width="9"/>
    </svg>
    <span style="margin-top:130px">Front Face</span>
  </div>

  <div class="face-label label-back">
    <svg width="80" height="195" viewBox="0 0 80 195" aria-hidden="true">
      <line x1="40" y1="0" x2="40" y2="181" stroke="#111" stroke-width="9"/>
      <polyline points="4,145 40,185 76,145" fill="none" stroke="#111" stroke-width="9"/>
    </svg>
    <span style="margin-bottom:30px">back Face</span>
  </div>

  <section class="back-face">
    <div class="brand"><span class="brand-dot"></span><span>Bright Spark Electrical Pty Ltd</span></div>
    <p class="tagline">Keep Me in your Wallet and pass Me on</p>
    <p class="phone">1300 574 862</p>
    <p class="licence">Lic No: 381946D</p>
  </section>

</div>
</body>
</html>
```